Thornfield Marsh, LLC Website

We are a small law firm in need of a website that contains the following:
1. Attractive main page
2. About us/attorney info for three people: Leonard Thornfield (attorney), Brent Marsh (attorney), and Melinda Carrow (legal assistant). We have bio's ready to submit.
3. Blog/video page. We'd like to post blogs and videos to help drive traffic
4. Multidistrict Litigation and Class Actions page, where we post information regarding active MDLs and Class actions that we are doing intake on.
Updates

Can you also please use the color "gold" in the design and logo? Thanks.

Industry/Entity Type

Legal

Coding

Coded - Design and coding required

Number of Pages Required

1 page

Colors
0054AA
0677BA
7BADD7
CADEEF
E8F1F8

Requirements
Must have
• 1. Attractive main page 2. About us/attorney info for three people: Leonard Thornfield (attorney), Brent Marsh (attorney), and Melinda Carrow (legal assistant). We have bio's ready to submit. 3. Blog/video page. We'd like to post blogs and videos to help drive traffic 4. Multidistrict Litigation and Class Actions page, where we post information regarding active MDLs and Class actions that we are doing intake on.

```html
<!DOCTYPE html>
<html lang="en">
<head>
<meta charset="utf-8">
<title>Thornfield Marsh, LLC — Lawyers</title>
<link rel="stylesheet" href="https://fonts.googleapis.com/css2?family=Outfit:wght@400;500;600;700&family=Inter:wght@400;500;600;700&display=swap">
<style>
:root{
  --gold:#c6a24a;
  --gold-dark:#a9842e;
  --gold-light:#e9d792;
  --ink:#111111;
  --text:#2b2b2b;
  --muted:#7a7a7a;
  --line:#e4e4e4;
  --soft:#f7f7f7;
  --white:#ffffff;
  --footer:#3b3b3b;
}
*{box-sizing:border-box;margin:0;padding:0}
html,body{width:1200px;height:4138px;overflow:hidden}
body{position:relative;background:var(--white);font-family:"Inter",sans-serif;color:var(--text)}
.abs{position:absolute}
.heading{font-family:"Outfit",sans-serif}
.label{font-family:"Outfit",sans-serif;font-weight:500;font-size:15px;letter-spacing:.3px;color:var(--ink);text-align:center}
.title{font-family:"Outfit",sans-serif;font-weight:600;font-size:40px;color:var(--gold);text-align:center}
.divider{display:flex;align-items:center;gap:6px;justify-content:center}
.divider span{width:32px;height:1.5px;background:var(--ink)}
.divider i{width:14px;height:6px;border-radius:3px;background:var(--ink)}
.body-copy{font-size:10.5px;line-height:19px;color:var(--muted)}
.btn-dark{display:inline-flex;align-items:center;justify-content:center;background:var(--ink);color:var(--white);font-size:10.5px;font-weight:600;border-radius:2px}
.btn-gold{display:inline-flex;align-items:center;justify-content:center;background:var(--gold);color:var(--ink);font-size:10.5px;font-weight:600;border-radius:2px}

/* header */
.logo{display:flex;align-items:center;gap:8px;font-family:"Inter",sans-serif;font-weight:700;font-size:15px;color:var(--ink)}
.logo b{width:26px;height:26px;background:var(--gold);display:block}
.social{display:flex;gap:8px}
.social span{width:28px;height:28px;border-radius:50%;background:var(--gold);display:flex;align-items:center;justify-content:center}
.call small{display:block;font-size:10px;color:var(--gold)}
.call strong{font-size:15px;font-weight:500;color:var(--ink)}
.nav{display:flex;gap:36px;font-size:10.5px;font-weight:600;color:var(--white);letter-spacing:.2px}
.nav a{color:inherit;text-decoration:none}

.side-tabs div{width:97px;height:50px;background:var(--ink);color:var(--white);font-size:11px;font-weight:600;display:flex;align-items:center;gap:8px;padding-left:16px;margin-bottom:2px}

/* awards */
.badges{display:grid;grid-template-columns:1fr 1fr;border:1px solid var(--line);background:var(--soft)}
.badges div{height:94px;border:1px solid var(--line);display:flex;align-items:center;justify-content:center;background:var(--white)}

/* practice */
.card{position:absolute;top:1741px;height:352px;overflow:hidden;color:var(--white);text-align:center}
.card .photo{position:absolute;inset:0;background:linear-gradient(180deg,#6d6d6d,#3e3e3e)}
.card .shade{position:absolute;inset:0;background:rgba(0,0,0,.35)}
.card h3{position:relative;font-family:"Outfit",sans-serif;font-weight:600;font-size:15px;line-height:21px;margin-top:82px;padding:0 10px}
.card .icon{position:absolute;top:36px;left:50%;transform:translateX(-50%)}
.card .dots{position:absolute;bottom:18px;left:50%;transform:translateX(-50%);display:flex;gap:3px}
.card .dots i{width:4px;height:4px;border-radius:50%;background:var(--gold)}
.card.active{top:1723px;height:388px;background:var(--gold);overflow:visible}
.card.active h3{margin-top:50px;font-size:14px}
.card.active p{font-size:10.5px;line-height:18.5px;padding:0 30px;margin-top:14px}

/* news */
.news-item{position:absolute;left:616px;width:452px;height:92px}
.news-item .thumb{position:absolute;left:0;top:0;width:127px;height:92px;background:linear-gradient(135deg,#9a9a9a,#3f3f3f)}
.news-item .meta{position:absolute;left:144px;top:0}
.news-item .date{font-size:9.5px;color:var(--gold)}
.news-item h4{font-size:13.5px;font-weight:600;color:var(--ink);margin:6px 0 8px}
.news-item p{font-size:10px;line-height:18px;color:var(--muted)}

/* form */
.field{position:absolute;border:1px solid var(--line);border-radius:2px;font-size:10px;color:var(--muted);padding:16px 18px}

/* footer */
.foot-col h5{font-family:"Inter",sans-serif;font-weight:600;font-size:13px;color:var(--gold);margin-bottom:14px}
.foot-col li{list-style:none;font-size:10.5px;color:#e6e6e6;line-height:21.5px}
.foot-col .gold{color:var(--gold)}
</style>
</head>
<body>

<!-- Hero background -->
<svg class="abs" style="left:0;top:0" width="1200" height="620" viewBox="0 0 1200 620" aria-hidden="false">
  <defs>
    <linearGradient id="heroGrad" x1="0" y1="0" x2="1" y2="0.3">
      <stop offset="0" stop-color="#b48d35"/>
      <stop offset="0.5" stop-color="#e3cf82"/>
      <stop offset="1" stop-color="#bb9741"/>
    </linearGradient>
    <linearGradient id="portraitGrad" x1="0" y1="0" x2="0" y2="1">
      <stop offset="0" stop-color="#c9b27a"/>
      <stop offset="1" stop-color="#2e3550"/>
    </linearGradient>
    <clipPath id="heroClip"><path d="M0 0H1200V548Q600 612 0 532Z"/></clipPath>
  </defs>
  <path d="M0 0H1200V548Q600 612 0 532Z" fill="url(#heroGrad)"/>
  <rect x="0" y="0" width="1200" height="68" fill="#ffffff"/>
  <line x1="0" y1="111" x2="1200" y2="111" stroke="#ffffff" stroke-opacity=".35"/>
  <g clip-path="url(#heroClip)">
    <rect role="img" aria-label="Photo of the firm's two attorneys standing side by side in suits" x="505" y="165" width="400" height="460" fill="url(#portraitGrad)" opacity=".85"/>
  </g>
  <circle cx="600" cy="580" r="26" fill="#ffffff" stroke="#c6a24a" stroke-width="2"/>
  <rect x="592" y="568" width="16" height="24" rx="8" fill="none" stroke="#c6a24a" stroke-width="1.8"/>
  <line x1="600" y1="573" x2="600" y2="578" stroke="#c6a24a" stroke-width="1.8"/>
</svg>

<!-- Header -->
<div class="abs logo" style="left:131px;top:20px">
  <b></b>THORNFIELD MARSH LLC
</div>
<div class="abs social" style="left:556px;top:20px">
  <span></span><span></span>
  <span><svg width="13" height="10" viewBox="0 0 13 10"><rect x=".6" y=".6" width="11.8" height="8.8" fill="none" stroke="#111" stroke-width="1.2"/><path d="M.6 .8L6.5 5.5 12.4 .8" fill="none" stroke="#111" stroke-width="1.2"/></svg></span>
</div>
<div class="abs call" style="left:706px;top:18px;display:flex;gap:8px;align-items:center">
  <svg width="28" height="28" viewBox="0 0 28 28"><circle cx="14" cy="14" r="14" fill="#c6a24a"/><path d="M10 8l2.5 2.5-1.5 2c1 2 2.5 3.5 4.5 4.5l2-1.5L20 18l-1.5 2C13 19.5 8.5 15 8 9.5Z" fill="none" stroke="#111" stroke-width="1.2"/></svg>
  <div><small>Call Us</small><strong>(555) 214-7730</strong></div>
</div>
<div class="abs btn-dark" style="left:898px;top:16px;width:170px;height:37px;color:var(--gold)">Get your free consultation</div>

<nav class="abs nav" style="left:0;width:1200px;top:84px;justify-content:center">
  <a>HOME</a><a>ABOUT US</a><a>ATTORNEYS</a><a>PRACTICE AREAS</a><a>RESOURCES</a><a>CONTACT US</a>
</nav>
<div class="abs" style="left:328px;top:108px;width:4px;height:4px;border-radius:50%;background:#fff"></div>

<!-- Hero copy -->
<h1 class="abs heading" style="left:131px;top:192px;font-size:58px;line-height:70px;font-weight:600;color:#fff">All-in-One<br>Legal Expertise</h1>
<p class="abs" style="left:131px;top:343px;width:380px;font-size:12px;line-height:20px;color:#fff">We offer expert legal support tailored to your unique needs, covering a wide range of practice areas including family law, business law, real estate, and more.</p>
<div class="abs btn-dark" style="left:131px;top:424px;width:138px;height:37px">Practice Areas</div>

<div class="abs side-tabs" style="left:1103px;top:250px">
  <div><svg width="13" height="13" viewBox="0 0 13 13"><path d="M2 1l3 3-1.5 2c1 2 2 3 4 4l2-1.5 3 3-1.5 1.5C5 12 1 8 .5 2.5Z" fill="none" stroke="#c6a24a" stroke-width="1.1"/></svg>PHONE</div>
  <div><svg width="13" height="10" viewBox="0 0 13 10"><rect x=".6" y=".6" width="11.8" height="8.8" fill="none" stroke="#c6a24a" stroke-width="1.1"/><path d="M.6 .8L6.5 5.5 12.4 .8" fill="none" stroke="#c6a24a" stroke-width="1.1"/></svg>EMAIL</div>
  <div><svg width="14" height="13" viewBox="0 0 14 13"><path d="M7 1C3.5 1 1 3.2 1 6c0 1.4.6 2.6 1.6 3.5L2 12l3-1.4c.6.2 1.3.3 2 .3 3.5 0 6-2.2 6-5S10.5 1 7 1Z" fill="none" stroke="#c6a24a" stroke-width="1.1"/></svg>CHAT</div>
</div>

<!-- Intro -->
<div class="abs label" style="left:0;width:1200px;top:657px">THORNFIELD MARSH LLC</div>
<h2 class="abs title" style="left:0;width:1200px;top:680px">Bayport Litigation Lawyers</h2>
<div class="abs divider" style="left:0;width:1200px;top:749px"><span></span><i></i><span></span></div>

<p class="abs body-copy" style="left:131px;top:808px;width:440px">Lorem ipsum dolor sit amet, consectetur adipiscing elit. Morbi placerat, odio at iaculis viverra, enim ante tristique urna, quis pulvinar nunc justo vel nisi. Duis dapibus massa nec neque luctus, sodales faucibus dolor gravida. Duis pulvinar ac odio eu dapibus. Quisque viverra felis id risus pellentesque, eget dapibus erat euismod. In ac est ut massa commodo blandit.</p>
<blockquote class="abs" style="left:131px;top:918px;width:440px;border-left:2px solid var(--ink);padding-left:16px;font-size:13.5px;line-height:22.5px;color:var(--text)">Duis dapibus massa nec neque luctus, sodales faucibus dolor gravida. Duis pulvinar ac odio eu dapibus. Quisque viverra felis id risus pellentesque, eget dapibus erat euismod. In ac est ut massa commodo blandit.</blockquote>
<p class="abs body-copy" style="left:131px;top:1028px;width:440px">Lorem ipsum dolor sit amet, consectetur adipiscing elit. Morbi placerat, odio at iaculis viverra, enim ante tristique urna, quis pulvinar nunc justo vel nisi. Duis dapibus massa nec neque luctus, sodales faucibus dolor gravida.</p>
<div class="abs btn-dark" style="left:133px;top:1108px;width:112px;height:37px">Learn More</div>

<div class="abs" style="left:654px;top:812px;width:414px;height:200px;background:var(--gold)"></div>
<div class="abs" role="img" aria-label="Black and white photo of hands signing documents beside a coffee cup" style="left:608px;top:822px;width:452px;height:339px;background:linear-gradient(135deg,#c9c9c9,#5e5e5e)"></div>

<!-- Awards -->
<div class="abs" style="left:0;top:1237px;width:1200px;height:1px;background:var(--line)"></div>
<div class="abs label" style="left:131px;top:1302px;text-align:left">ACHIEVEMENT</div>
<h2 class="abs title" style="left:131px;top:1324px;text-align:left">Awards &amp; Recognitions</h2>
<div class="abs divider" style="left:131px;top:1382px;justify-content:flex-start"><span></span><i></i><span></span></div>
<p class="abs body-copy" style="left:131px;top:1415px;width:455px">Lorem ipsum dolor sit amet, consectetur adipiscing elit. Morbi placerat, odio at iaculis viverra, enim ante tristique urna, quis pulvinar nunc justo vel nisi. Duis dapibus massa nec neque luctus, sodales faucibus dolor gravida.</p>
<div class="abs badges" style="left:662px;top:1290px;width:408px">
  <div><svg width="66" height="66" viewBox="0 0 66 66" role="img" aria-label="Lawyer rating badge"><path d="M8 6H58V46L33 62 8 46Z" fill="#2b2b2b"/></svg></div>
  <div><svg width="150" height="40" viewBox="0 0 150 40" role="img" aria-label="Peer rating badge"><rect x="0" y="6" width="150" height="30" fill="#2b2b2b"/></svg></div>
  <div><svg width="110" height="40" viewBox="0 0 110 40" role="img" aria-label="Rising stars listing badge"><rect x="0" y="6" width="110" height="28" rx="3" fill="#3f3f3f"/></svg></div>
  <div><svg width="120" height="48" viewBox="0 0 120 48" role="img" aria-label="Client review listing badge"><rect x="0" y="6" width="120" height="36" rx="4" fill="#111"/></svg></div>
</div>

<!-- Practice areas -->
<div class="abs" style="left:0;top:1532px;width:1200px;height:933px;background:var(--soft)"></div>
<div class="abs label" style="left:0;width:1200px;top:1592px">EXPERTISE</div>
<h2 class="abs title" style="left:0;width:1200px;top:1614px">Practice Areas</h2>
<div class="abs divider" style="left:0;width:1200px;top:1685px"><span></span><i></i><span></span></div>

<div class="card" style="left:0;width:213px">
  <div class="photo" role="img" aria-label="Damaged car after a road accident"></div><div class="shade"></div>
  <svg class="icon" width="40" height="34" viewBox="0 0 40 34"><path d="M4 30H36M10 22h20l-3-8H13Z" fill="none" stroke="#c6a24a" stroke-width="1.6"/><circle cx="14" cy="26" r="3" fill="none" stroke="#c6a24a" stroke-width="1.6"/><circle cx="26" cy="26" r="3" fill="none" stroke="#c6a24a" stroke-width="1.6"/></svg>
  <h3>Auto Accident, Homeowner &amp; Business Owner Insurance Claims</h3>
  <div class="dots"><i></i><i></i><i></i></div>
</div>
<div class="card" style="left:213px;width:203px">
  <div class="photo" role="img" aria-label="Construction workers in safety vests"></div><div class="shade"></div>
  <svg class="icon" width="36" height="36" viewBox="0 0 36 36"><circle cx="18" cy="13" r="7" fill="none" stroke="#c6a24a" stroke-width="1.6"/><path d="M6 33c1-7 6-11 12-11s11 4 12 11" fill="none" stroke="#c6a24a" stroke-width="1.6"/></svg>
  <h3>Employment Law, Wage and Hour &amp; Workers' Compensation</h3>
  <div class="dots"><i></i><i></i><i></i></div>
</div>
<div class="card active" style="left:416px;width:236px">
  <h3>General Litigation</h3>
  <p>Lorem ipsum dolor sit amet, consectetur adipiscing elit. Morbi placerat, odio at iaculis viverra, enim ante tristique urna, quis pulvinar nunc justo vel nisi. Duis dapibus massa nec neque luctus, sodales faucibus dolor gravida.</p>
  <div class="btn-dark" style="margin-top:36px;width:150px;height:37px">Learn More</div>
  <div class="dots" style="bottom:38px"><i style="background:#111"></i><i style="background:#111"></i><i style="background:#111"></i></div>
</div>
<div class="card" style="left:652px;width:203px">
  <div class="photo" role="img" aria-label="Hand pressing a stamp onto paperwork"></div><div class="shade"></div>
  <svg class="icon" width="34" height="38" viewBox="0 0 34 38"><rect x="5" y="3" width="22" height="30" fill="none" stroke="#c6a24a" stroke-width="1.6"/><path d="M10 12h12M10 18h12M10 24h8" stroke="#c6a24a" stroke-width="1.6"/></svg>
  <h3>Collections</h3>
  <div class="dots"><i></i><i></i><i></i></div>
</div>
<div class="card" style="left:855px;width:213px">
  <div class="photo" role="img" aria-label="Doctor's stethoscope with handcuffs"></div><div class="shade"></div>
  <svg class="icon" width="38" height="36" viewBox="0 0 38 36"><rect x="6" y="6" width="14" height="26" rx="7" transform="rotate(-35 13 19)" fill="none" stroke="#c6a24a" stroke-width="1.6"/><circle cx="27" cy="22" r="8" fill="none" stroke="#c6a24a" stroke-width="1.6"/></svg>
  <h3>Medicare Fraud</h3>
  <div class="dots"><i></i><i></i><i></i></div>
</div>
<div class="card" style="left:1068px;width:132px">
  <div class="photo" role="img" aria-label="Two people shaking hands over a desk"></div><div class="shade"></div>
  <svg class="icon" style="left:66px" width="40" height="34" viewBox="0 0 40 34"><circle cx="10" cy="20" r="4" fill="none" stroke="#c6a24a" stroke-width="1.6"/><circle cx="20" cy="20" r="4" fill="none" stroke="#c6a24a" stroke-width="1.6"/><circle cx="30" cy="20" r="4" fill="none" stroke="#c6a24a" stroke-width="1.6"/><path d="M8 8l12 6 12-6" fill="none" stroke="#c6a24a" stroke-width="1.6"/></svg>
  <h3 style="text-align:left;padding-left:58px;white-space:nowrap">Mediation and<br>Arbitration</h3>
  <div class="dots" style="left:110px"><i></i><i></i><i></i></div>
</div>

<!-- Contact callout -->
<div class="abs" style="left:148px;top:2172px;width:904px;height:240px;border:1.5px solid var(--gold)"></div>
<div class="abs label" style="left:548px;width:104px;top:2162px;background:var(--soft)">CONTACT</div>
<h2 class="abs heading" style="left:0;width:1200px;top:2198px;text-align:center;font-size:31px;line-height:44px;font-weight:600;color:var(--gold)">Get in Touch with Our Top Attorney Today<br>for Any Legal Assistance</h2>
<p class="abs" style="left:0;width:1200px;top:2300px;text-align:center;font-size:10px;color:var(--muted)">To schedule a free initial consultation, we will provide sound legal advice without judgment. Contact us today at <b style="color:var(--ink)">123 456 7890</b></p>
<div class="abs btn-dark" style="left:526px;top:2339px;width:148px;height:36px">Get in Touch</div>

<!-- News -->
<div class="abs label" style="left:0;width:1200px;top:2517px">WHAT'S NEW</div>
<h2 class="abs title" style="left:0;width:1200px;top:2539px">Latest News &amp; Updates</h2>
<div class="abs divider" style="left:0;width:1200px;top:2608px"><span></span><i></i><span></span></div>

<div class="abs" role="img" aria-label="Three colleagues in business attire reviewing papers in an office corridor" style="left:131px;top:2654px;width:452px;height:264px;background:linear-gradient(135deg,#d8d3c6,#6c6a66)"></div>
<div class="abs" style="left:532px;top:2670px;width:36px;height:38px;background:var(--gold);color:#fff;font-size:8px;font-weight:600;text-align:center;line-height:10px;padding-top:5px">11<br>APRIL<br>2025</div>
<h3 class="abs" style="left:131px;top:2938px;width:452px;font-size:14px;line-height:22px;font-weight:600;color:var(--ink)">Lorem ipsum dolor sit amet, consectetur adipiscing elit. Morbi placerat, odio at iaculis viverra.</h3>
<p class="abs body-copy" style="left:131px;top:2986px;width:452px">Lorem ipsum dolor sit amet, consectetur adipiscing elit. Morbi placerat, odio at iaculis viverra, enim ante tristique urna, quis pulvinar nunc justo vel nisi. Duis dapibus massa nec neque luctus, sodales faucibus dolor gravida.</p>
<div class="abs" style="left:131px;top:3056px;font-size:10.5px;font-weight:600;color:var(--gold)">Learn More →</div>

<div class="news-item" style="top:2654px"><div class="thumb" role="img" aria-label="Judge's gavel on a desk"></div><div class="meta"><div class="date">11 APRIL, 2025</div><h4>Lorem ipsum dolor sit amet, adipiscing</h4><p>Morbi placerat, odio at iaculis viverra, enim ante tristique<br>urna, quis pulvinar nunc justo...</p></div></div>
<div class="news-item" style="top:2761px"><div class="thumb" role="img" aria-label="Handshake over a contract"></div><div class="meta"><div class="date">11 APRIL, 2025</div><h4>Lorem ipsum dolor sit amet, adipiscing</h4><p>Morbi placerat, odio at iaculis viverra, enim ante tristique<br>urna, quis pulvinar nunc justo...</p></div></div>
<div class="news-item" style="top:2868px"><div class="thumb" role="img" aria-label="Hands reviewing legal papers"></div><div class="meta"><div class="date">11 APRIL, 2025</div><h4>Lorem ipsum dolor sit amet, adipiscing</h4><p>Morbi placerat, odio at iaculis viverra, enim ante tristique<br>urna, quis pulvinar nunc justo...</p></div></div>
<div class="news-item" style="top:2975px"><div class="thumb" role="img" aria-label="Lawyers meeting at a table"></div><div class="meta"><div class="date">11 APRIL, 2025</div><h4>Lorem ipsum dolor sit amet, adipiscing</h4><p>Morbi placerat, odio at iaculis viverra, enim ante tristique<br>urna, quis pulvinar nunc justo...</p></div></div>

<!-- Consultation -->
<div class="abs" role="img" aria-label="Grey toned photo of courthouse columns" style="left:0;top:3124px;width:1200px;height:386px;background:linear-gradient(120deg,#9c9c9c,#5a5a5a 55%,#7d7d7d)"></div>
<div class="abs" style="left:131px;top:3289px;width:937px;height:445px;background:#fff;box-shadow:0 6px 24px rgba(0,0,0,.08)"></div>
<div class="abs label" style="left:0;width:1200px;top:3337px">GET IN TOUCH</div>
<h2 class="abs title" style="left:0;width:1200px;top:3360px">Request Free Consultation</h2>
<div class="abs divider" style="left:0;width:1200px;top:3427px"><span></span><i></i><span></span></div>
<div class="field" style="left:186px;top:3475px;width:267px;height:48px">Name</div>
<div class="field" style="left:466px;top:3475px;width:267px;height:48px">Phone</div>
<div class="field" style="left:747px;top:3475px;width:268px;height:48px">Email</div>
<div class="field" style="left:186px;top:3537px;width:829px;height:75px">Message</div>
<div class="abs btn-gold" style="left:529px;top:3633px;width:142px;height:36px">Submit Now</div>

<!-- Footer -->
<svg class="abs" style="left:0;top:3780px" width="1200" height="358" viewBox="0 0 1200 358">
  <defs><linearGradient id="footGrad" x1="0" y1="0" x2="1" y2="1"><stop offset="0" stop-color="#2e2e2e"/><stop offset="1" stop-color="#555"/></linearGradient></defs>
  <path d="M0 55Q600 -12 1200 55V358H0Z" fill="url(#footGrad)"/>
  <line x1="0" y1="297" x2="1200" y2="297" stroke="#ffffff" stroke-opacity=".15"/>
  <circle cx="600" cy="20" r="26" fill="#ffffff" stroke="#c6a24a" stroke-width="2"/>
  <path d="M591 24L600 15 609 24" fill="none" stroke="#c6a24a" stroke-width="2"/>
</svg>

<div class="abs logo" style="left:131px;top:3882px;color:#fff"><b></b>THORNFIELD MARSH LLC</div>
<div class="abs" style="left:131px;top:3948px;font-size:12px;font-weight:600;color:var(--gold)">Follow Us</div>
<div class="abs social" style="left:131px;top:3978px">
  <span></span><span></span>
  <span><svg width="13" height="10" viewBox="0 0 13 10"><rect x=".6" y=".6" width="11.8" height="8.8" fill="none" stroke="#111" stroke-width="1.2"/><path d="M.6 .8L6.5 5.5 12.4 .8" fill="none" stroke="#111" stroke-width="1.2"/></svg></span>
</div>

<div class="abs foot-col" style="left:445px;top:3872px">
  <h5>Practice Areas</h5>
  <ul><li>Accident</li><li>Employment Law</li><li>General Litigation</li><li>Collections</li><li>Medicare Fraud</li><li>Mediation and Arbitration</li></ul>
</div>
<div class="abs foot-col" style="left:680px;top:3872px">
  <h5>About</h5>
  <ul><li>About Attorney</li><li>Press Release</li><li>Contact</li><li>News</li></ul>
</div>
<div class="abs foot-col" style="left:861px;top:3872px">
  <h5>Contact</h5>
  <ul style="line-height:14px">
    <li style="line-height:14px">Address</li>
    <li class="gold" style="line-height:14px">482 Harbor Row</li>
    <li class="gold" style="line-height:14px;margin-bottom:6px">Bayport, AL 36690</li>
    <li>Thornfield : <span class="gold">(555) 214-7730</span></li>
    <li>Marsh : <span class="gold">(555) 214-7730</span></li>
  </ul>
</div>

<div class="abs" style="left:0;width:1200px;top:4100px;text-align:center;font-size:10.5px;color:#dcdcdc">Copyright © 2025, Thornfield, Marsh LLC</div>

</body>
</html>
```